School Communication Email Template

Looking for a designer to create a couple simple email templates that are matching our brand colors and feel. Attached is the default email template that is currently being sent out. Company details can be shared upon request.

Template is to be used within the booking tool we use (snapshot below) and gmail. Template code is in HTML (see screenshot below).
Updates

Template code for website should be in HTML. Sorry if that created confusion.

Target Market(s)

Parents of kids enrolled in our classes

Industry/Entity Type

Kids sport classes

Font styles to use
Serif

Colors
0054AA
0677BA
7BADD7
CADEEF
E8F1F8
FFF300
FFF600
FEFA6F
FFFEC7
FFFEE8

Requirements
Must have
• Consistency with company brand/colors
Nice to have
• Flexibility to be adjusted as needed

```html
<!DOCTYPE html>
<html lang="en">
<head>
<meta charset="utf-8">
<title>Booking Email Template</title>
<link href="https://fonts.googleapis.com/css2?family=Montserrat:wght@400;600;700;800&family=Open+Sans:wght@400;600&display=swap" rel="stylesheet">
<style>
  :root {
    --page: #e9e9e9;
    --white: #ffffff;
    --navy: #1f3a8a;
    --navy-deep: #233d85;
    --navy-band: #2c4592;
    --blue-text: #2a4aa8;
    --yellow: #f9c22e;
    --amber: #f2b31c;
    --photo-warm: #c9a27e;
    --photo-cool: #d9d2c8;
  }
  * { box-sizing: border-box; margin: 0; padding: 0; }
  html, body { width: 739px; height: 1200px; overflow: hidden; }
  body {
    background: var(--page);
    font-family: "Montserrat", Arial, sans-serif;
    position: relative;
  }
  .email {
    position: absolute;
    left: 160px; top: 94px;
    width: 419px; height: 1051px;
    background: var(--white);
    box-shadow: 0 4px 14px rgba(0,0,0,0.18);
    overflow: hidden;
  }
  .hero {
    position: absolute; left: 0; top: 0; width: 419px; height: 251px;
    background: linear-gradient(90deg, #e6a93a 0%, var(--photo-warm) 35%, var(--photo-cool) 70%, #b9b2a8 100%);
  }
  .hero-tagline {
    position: absolute; left: 20px; top: 120px; width: 190px;
    color: var(--white); font-weight: 700; font-size: 15px; line-height: 1.3;
  }
  .brand {
    position: absolute; right: 12px; bottom: 14px;
    display: flex; align-items: center; gap: 6px;
    color: var(--navy); font-weight: 800; font-size: 13px;
  }
  .brand-dot { width: 14px; height: 14px; border-radius: 50%; background: var(--yellow); }
  .cta {
    position: absolute; left: 69px; top: 258px; width: 281px; height: 37px;
    background: var(--navy-deep); color: var(--white);
    font-weight: 700; font-size: 15px; letter-spacing: 0.3px;
    display: flex; align-items: center; justify-content: center;
  }
  .phone {
    position: absolute; left: 0; top: 306px; width: 419px; text-align: center;
    color: var(--amber); font-weight: 800; font-size: 22px;
  }
  .section-title {
    position: absolute; left: 20px; top: 361px;
    color: var(--navy); font-weight: 700; font-size: 17px;
  }
  .booking-rows { position: absolute; left: 20px; top: 408px; list-style: none; }
  .booking-row { display: flex; align-items: center; height: 29.6px; }
  .row-label {
    width: 108px; height: 20px; background: var(--navy-deep); color: var(--white);
    font-weight: 700; font-size: 11.5px; padding-left: 8px;
    display: flex; align-items: center;
    border-radius: 0 10px 10px 0;
  }
  .row-value { margin-left: 47px; color: var(--blue-text); font-family: "Open Sans", Arial, sans-serif; font-size: 14px; }
  .band { position: absolute; left: 0; top: 700px; }
  .band-title {
    position: absolute; left: 20px; top: 727px;
    color: var(--white); font-weight: 700; font-size: 14px;
  }
  .columns {
    position: absolute; left: 20px; top: 760px; width: 380px;
    display: flex; gap: 0;
  }
  .column { width: 190px; padding-right: 14px; color: var(--white); }
  .column + .column { border-left: 1px solid rgba(255,255,255,0.7); padding-left: 18px; padding-right: 0; }
  .column h3 { font-size: 14px; font-weight: 700; margin-bottom: 5px; }
  .column p { font-family: "Open Sans", Arial, sans-serif; font-size: 10px; line-height: 1.38; }
  .footer {
    position: absolute; left: 0; top: 953px; width: 419px; height: 98px;
    background: var(--yellow);
    display: flex; justify-content: space-around; align-items: center;
    padding: 0 10px;
  }
  .footer-item { display: flex; flex-direction: column; align-items: center; gap: 7px; color: var(--white); font-weight: 700; font-size: 11px; }
  .footer-icon { width: 18px; height: 18px; border-radius: 50%; border: 1.5px solid var(--white); }
  .social { display: flex; gap: 7px; }
  .social span { width: 18px; height: 18px; border-radius: 50%; background: var(--white); opacity: 0.9; }
</style>
</head>
<body>
  <main class="email">
    <div class="hero" role="img" aria-label="Photo of three smiling girls looking at a phone together">
      <p class="hero-tagline">Established in 1984 by Martin Hale, A renowned Agent.</p>
      <div class="brand"><span class="brand-dot"></span>Sprint Kids</div>
    </div>

    <div class="cta">SCHEDULE A MEETING</div>
    <p class="phone">+20 11 4400</p>

    <h2 class="section-title">BOOKING</h2>
    <ul class="booking-rows">
      <li class="booking-row"><span class="row-label">STUDENT:</span><span class="row-value">lorem ipsum</span></li>
      <li class="booking-row"><span class="row-label">APPOINTMENT:</span><span class="row-value">lorem ipsum</span></li>
      <li class="booking-row"><span class="row-label">SERVICE:</span><span class="row-value">lorem ipsum</span></li>
      <li class="booking-row"><span class="row-label">START DATE:</span><span class="row-value">lorem ipsum</span></li>
      <li class="booking-row"><span class="row-label">END DATE:</span><span class="row-value">lorem ipsum</span></li>
      <li class="booking-row"><span class="row-label">START TIME:</span><span class="row-value">lorem ipsum</span></li>
      <li class="booking-row"><span class="row-label">END TIME:</span><span class="row-value">lorem ipsum</span></li>
    </ul>

    <svg class="band" width="419" height="253" viewBox="0 0 419 253" role="img" aria-label="Faint photo of children in class under a blue overlay">
      <defs>
        <linearGradient id="bandShade" x1="0" y1="0" x2="1" y2="1">
          <stop offset="0" stop-color="#2c4592"/>
          <stop offset="0.6" stop-color="#354f9c"/>
          <stop offset="1" stop-color="#2a428d"/>
        </linearGradient>
      </defs>
      <polygon points="0,60 419,0 419,253 0,253" fill="url(#bandShade)"/>
    </svg>
    <h2 class="band-title">BOOKING</h2>

    <div class="columns">
      <section class="column">
        <h3>BOOKING</h3>
        <p>Lorem ipsum dolor sit amet consectetur adipiscing elit, sed diam nonummy nibh euismod tincidunt ut laoreet dolore magna aliquam erat volutpat. Ut wisi enim ad minim veniam, quis nostrud exerci tation ullamcorper suscipit lobortis nisl ut aliquip ex ea commodo consequat.</p>
      </section>
      <section class="column">
        <h3>BOOKING</h3>
        <p>Lorem ipsum dolor sit amet consectetur adipiscing elit, sed diam nonummy nibh euismod tincidunt ut laoreet dolore magna aliquam erat volutpat. Ut wisi enim ad minim veniam, quis nostrud exerci tation ullamcorper suscipit lobortis nisl ut aliquip ex ea commodo consequat.</p>
      </section>
    </div>

    <footer class="footer">
      <div class="footer-item"><span class="footer-icon"></span>REVIEWS</div>
      <div class="footer-item"><span class="footer-icon"></span>CONTACT US</div>
      <div class="footer-item">
        <div class="social"><span></span><span></span><span></span><span></span></div>
        CHECK OUR SOCIAL MEDIA
      </div>
    </footer>
  </main>
</body>
</html>
```